Banner dimension 1767 X 887 for Tolvenko website

Need one banner for our website www.tolvenko.com.au, The dimension of the banner should be 1767 x 887. Attached to this brief are two images that needs to be on that one banner, PLEASE DO NOT SEND SEPARATE BANNERS, both images on the same banner. Thanks

The banner should have the following message on it:

1.) " Take a further 40% off all stock" ( use code: TOLVENKO. Ends 31/12/2015)
2.) " Kick back or kick it up a notch this Autumn in the most versatile pique striped polo shirts and Pinafore belt strap denim dress"

Target Market(s)

kids aged 5-12yrs

Requirements
Must have
• very playful

```html
<!DOCTYPE html>
<html lang="en">
<head>
<meta charset="utf-8">
<title>Tolvenko – Take a further 40% off all stock</title>
<link rel="stylesheet" href="https://fonts.googleapis.com/css2?family=Barlow+Condensed:wght@300;400;700&display=swap">
<style>
  :root {
    --sky: #22a7cd;
    --sky-deep: #1f9ec5;
    --floor: #1b8fb3;
    --floor-deep: #177fa1;
    --sun: #ffd500;
    --white: #ffffff;
    --ink-blue: #23a6cc;
    --photo-top: #2f5d4a;
    --photo-mid: #5b86a8;
    --photo-low: #8fb0c8;
  }
  * { margin: 0; padding: 0; box-sizing: border-box; }
  html, body { width: 1200px; height: 602px; overflow: hidden; }
  body { font-family: "Barlow Condensed", "Arial Narrow", sans-serif; }

  .banner {
    position: relative;
    width: 1200px;
    height: 602px;
    overflow: hidden;
    background: linear-gradient(180deg, var(--sky) 0%, var(--sky-deep) 80%);
  }
  .floor {
    position: absolute;
    left: 0; right: 0; top: 483px; bottom: 0;
    background: linear-gradient(180deg, var(--floor) 0%, var(--floor-deep) 100%);
  }

  .kids-photo {
    position: absolute;
    left: 372px; top: 40px;
    width: 380px; height: 530px;
    border-radius: 14px;
    background: linear-gradient(180deg, var(--photo-top) 0%, var(--photo-mid) 45%, var(--photo-low) 100%);
  }

  .offer {
    position: absolute;
    left: 28px; top: 92px;
    color: var(--white);
    text-transform: uppercase;
    white-space: nowrap;
  }
  .offer__lead {
    font-weight: 700;
    font-size: 60px;
    line-height: 1;
    letter-spacing: -0.5px;
  }
  .offer__figure {
    font-weight: 700;
    font-size: 217px;
    line-height: 0.8;
    letter-spacing: -5px;
    color: var(--sun);
    margin-top: 22px;
  }
  .offer__tail {
    font-weight: 700;
    font-size: 63px;
    line-height: 1;
    margin-top: 8px;
    letter-spacing: -0.5px;
  }
  .offer__code {
    font-weight: 400;
    font-size: 26px;
    line-height: 1;
    margin-top: 12px;
  }

  .promo-panel {
    position: absolute;
    left: 752px; top: 48px;
    width: 448px; height: 418px;
  }
  .promo-panel svg { display: block; }
  .promo-copy {
    position: absolute;
    left: 776px; top: 112px;
    color: var(--ink-blue);
    text-transform: uppercase;
    white-space: nowrap;
    transform: rotate(-4.6deg);
    transform-origin: left top;
  }
  .promo-copy__intro {
    font-weight: 400;
    font-size: 40px;
    line-height: 44px;
  }
  .promo-copy__products {
    font-weight: 700;
    font-size: 48px;
    line-height: 58px;
    margin-top: 10px;
  }
</style>
</head>
<body>
  <main class="banner">
    <div class="floor"></div>

    <div class="kids-photo" role="img" aria-label="Photo of a smiling boy in a striped polo shirt and denim shorts posing playfully beside a girl in a white tee and denim pinafore dress"></div>

    <section class="offer">
      <p class="offer__lead">Take a further</p>
      <p class="offer__figure">40%</p>
      <p class="offer__tail">Off all stock</p>
      <p class="offer__code">Use code: TOLVENKO. Ends 31/12/2015</p>
    </section>

    <div class="promo-panel">
      <svg width="448" height="418" viewBox="0 0 448 418" aria-hidden="true">
        <polygon points="0,42 448,4 448,376 2,414" fill="var(--sun)"/>
      </svg>
    </div>

    <section class="promo-copy">
      <p class="promo-copy__intro">Kick back or kick it up<br>a notch this autumn in<br>the most versatile pique</p>
      <p class="promo-copy__products">Striped polo shirts<br>and pinafore belt<br>strap denim dress</p>
    </section>
  </main>
</body>
</html>
```